Create a Graphic About YOURSELF and PixelHarbor

PixelHarbor would like you (designers) to create an awesome graphic to promote YOURSELF and your profile on PixelHarbor!

Your graphic should communicate your name, your services and should mention PixelHarbor.

The design should be perfect for sharing on Chatterly. Here's an example of what we'd like http://blog.pixelharbor-example.ca/article/333/pixelharbor-launches-3000-hire-me-social-design-contest

Once you submitted your design, we'd love you to share the design ('advertisement') and promote yourself and PixelHarbor to your friends and potential customers. So make your submissions great and get your friends to vote for your design by 'Liking' it on Chatterly!

Prizes:
$1500 - "PixelHarbor Community" prize awarded to the designer with the most Chatterly 'Likes'
5 x $50 for the next 5 'most liked' designs on Chatterly

$1000 - "Hire Me" prize awarded to the designer who receives the most client invites
5 x $50 for the next 5 'most invited' designers

In summary, this is a great opportunity for you to increase your exposure to PixelHarbor customers and win cash prizes. Show off your design skills and get hired by PixelHarbor customers from around the world!

Target Market(s)

Fans, friends and customers of YOU

Industry/Entity Type

Cash

Requirements
Must have
• 1) Include your PixelHarbor user name on the graphic so customers can find you in the PixelHarbor Designer Directory
2) Include the tagline "Hire Me on PixelHarbor.com!" in your graphic design.
3) Share your design's URL on our Chatterly wall at http://chatterly-example.com/pixelharbor and get your friends to 'like' your design.
Nice to have
• 1) Include a tagline that expresses your design approach/philosophy
2) Artwork dimensions: 403 x 403 px
3) You can submit more than 1 design!
Should not have
• You must own the copyright of any images you use including stock imagery.

```html
<!DOCTYPE html>
<html lang="en">
<head>
<meta charset="utf-8">
<title>Pixel Harbor – The Creative Hand</title>
<link rel="stylesheet" href="https://fonts.googleapis.com/css2?family=Aldrich&display=swap">
<style>
  :root {
    --page: #ffffff;
    --teal: #2aa5b3;
    --teal-deep: #1f7f8a;
    --ink: #231f20;
    --white: #ffffff;
  }
  * { margin: 0; padding: 0; box-sizing: border-box; }
  html, body {
    width: 1200px;
    height: 552px;
    overflow: hidden;
    background: var(--page);
  }
  .canvas {
    position: relative;
    width: 1200px;
    height: 552px;
    background: var(--page);
    font-family: "Aldrich", sans-serif;
  }
  .banner {
    position: absolute;
    left: 72px;
    top: 63px;
    width: 1048px;
    height: 424px;
    background: var(--teal);
    overflow: hidden;
  }
  .hand-art {
    position: absolute;
    left: 0;
    top: 6px;
    width: 585px;
    height: 345px;
  }
  .headline {
    position: absolute;
    right: 52px;
    top: 44px;
    text-align: right;
    color: var(--white);
    font-size: 56px;
    line-height: 66px;
    letter-spacing: 0.5px;
    font-weight: 400;
    text-shadow: 2px 2px 0 rgba(35, 31, 32, 0.45);
  }
  .site-url {
    position: absolute;
    right: 54px;
    top: 186px;
    color: var(--ink);
    font-size: 29px;
    letter-spacing: 0.5px;
  }
  .hire-tagline {
    position: absolute;
    right: 54px;
    top: 240px;
    color: var(--white);
    font-size: 26px;
    letter-spacing: 0.5px;
  }
  .studio-mark {
    position: absolute;
    left: 34px;
    top: 342px;
    width: 62px;
    height: 62px;
    border-radius: 50%;
    background: var(--ink);
  }
  .studio-line {
    position: absolute;
    left: 165px;
    top: 366px;
    color: var(--ink);
    font-size: 33px;
    letter-spacing: 1.6px;
    white-space: nowrap;
  }
</style>
</head>
<body>
  <main class="canvas">
    <section class="banner">
      <svg class="hand-art" viewBox="0 0 585 345" role="img" aria-label="Illustration of a dark open hand reaching to the right with a white offset shadow">
        <defs>
          <linearGradient id="handTone" x1="0" y1="0" x2="1" y2="0">
            <stop offset="0" stop-color="#231f20" stop-opacity="0.9"/>
            <stop offset="0.55" stop-color="#231f20" stop-opacity="0.55"/>
            <stop offset="1" stop-color="#1f7f8a" stop-opacity="0"/>
          </linearGradient>
        </defs>
        <path d="M0 95 L200 40 Q300 0 400 15 L585 120 L585 300 Q470 345 360 335 L0 250 Z" fill="url(#handTone)"/>
      </svg>

      <h1 class="headline">pixel harbor the<br>creative hand</h1>
      <p class="site-url">pixelharbor.com.au</p>
      <p class="hire-tagline">Hire Me on PixelHarbor.com!</p>

      <div class="studio-mark" aria-hidden="true"></div>
      <p class="studio-line">brushfield studio design, marketing, &amp; more</p>
    </section>
  </main>
</body>
</html>
```